Business Card Design

I need a business card, for my company that reflects fire and building.
I am a bushfire consultant, and my role is to determine a fire assessment for new houses being built, in bushfire prone areas.
Compiling a report on what building materials will need to be used, and whether or not parts of the block will need to be cleared of vegetation. I would like to see the colours of fire, and possibly a house on there as well, or maybe just fire. This will probably be used as a logo as well, and will reflect the severity of fire to housing.
Target Market(s)
New home builders residential
Industry/Entity Type
Building
Contact Information for Business Card
Emberline Advisory Group
Bushfire Consultant
Garth Pellowe
0438 612 904

```html
<!DOCTYPE html>
<html lang="en">
<head>
<meta charset="UTF-8">
<title>Emberline Advisory Group — Business Card</title>
<link rel="stylesheet" href="https://fonts.googleapis.com/css2?family=Lilita+One&family=Kaushan+Script&family=Arimo:wght@400&display=swap">
<style>
  :root {
    --canvas-bg: #ffffff;
    --band-deep: #6e1208;
    --band-mid: #a3240c;
    --panel-light: #f7a23a;
    --panel-mid: #ea6a1c;
    --panel-dark: #c8400f;
    --back-centre: #f6a03a;
    --back-mid: #e2601a;
    --back-edge: #8c1e0a;
    --card-border: #d8cfc8;
    --ink-light: #ffffff;
    --ink-contact: #5a1608;
  }
  * { margin: 0; padding: 0; box-sizing: border-box; }
  html, body {
    width: 1200px;
    height: 370px;
    overflow: hidden;
    background: var(--canvas-bg);
  }
  .canvas {
    position: relative;
    width: 1200px;
    height: 370px;
  }
  .card {
    position: absolute;
    top: 5px;
    width: 585px;
    height: 358px;
    border: 1px solid var(--card-border);
    overflow: hidden;
  }
  .card--front { left: 5px; background: var(--ink-light); }
  .card--back {
    left: 610px;
    background: radial-gradient(ellipse at 50% 55%, var(--back-centre) 0%, var(--back-mid) 45%, var(--back-edge) 100%);
    display: flex;
    align-items: center;
    justify-content: center;
  }
  .front__panel {
    position: absolute;
    left: 0; top: 0;
    width: 100%;
    height: 250px;
    background: linear-gradient(180deg, var(--panel-dark) 0%, var(--panel-light) 50%, var(--panel-mid) 100%);
  }
  .front__band {
    position: absolute;
    left: 0; top: 0;
    width: 100%;
    height: 125px;
  }
  .brand-name {
    font-family: "Lilita One", "Arial Black", sans-serif;
    color: var(--ink-light);
    font-weight: 400;
    letter-spacing: 0.5px;
    white-space: nowrap;
  }
  .front__brand {
    position: absolute;
    left: 34px;
    top: 14px;
    font-size: 42px;
  }
  .front__statement {
    position: absolute;
    left: 55px;
    top: 138px;
    width: 470px;
    font-family: "Kaushan Script", cursive;
    font-size: 21px;
    line-height: 30px;
    color: var(--ink-light);
  }
  .front__contact {
    position: absolute;
    left: 22px;
    top: 278px;
    font-family: "Arimo", Arial, sans-serif;
    font-style: normal;
    font-size: 15px;
    line-height: 19px;
    color: var(--ink-contact);
  }
  .back__brand { font-size: 38px; }
</style>
</head>
<body>
  <main class="canvas">
    <section class="card card--front" aria-label="Card front">
      <div class="front__panel"></div>
      <svg class="front__band" viewBox="0 0 585 125" preserveAspectRatio="none" aria-hidden="true">
        <defs>
          <linearGradient id="bandShade" x1="0" y1="0" x2="0" y2="1">
            <stop offset="0" stop-color="#6e1208"/>
            <stop offset="1" stop-color="#a3240c"/>
          </linearGradient>
        </defs>
        <path d="M0 0 H585 V92 C430 120 180 112 0 100 Z" fill="url(#bandShade)"/>
      </svg>
      <h1 class="brand-name front__brand">Emberline Advisory Group</h1>
      <p class="front__statement">Bushfire consultant and my role is to determine a fire assessment for new houses being built, in bushfire prone areas.</p>
      <address class="front__contact">
        Emberline Advisory Group<br>
        Bushfire Consultant<br>
        Garth Pellowe 0438 612 904
      </address>
    </section>

    <section class="card card--back" aria-label="Card back">
      <h2 class="brand-name back__brand">Emberline Advisory Group</h2>
    </section>
  </main>
</body>
</html>
```